Gardener needs an exciting new flyer design.

I'm a passionate gardener that requires a custom flyer design for a owner operator gardening business. Design will be for a DL flyer. I'm based on the Sunshine coast in Queensland Australia. My target audience is the residential market on the Sunshine coast. Business name is Tollmere Yards. My services are, lawn mowing, weeding, Eco Friendly fertilizing, green waste removal, Mulching, tree and shrub pruning, Full garden makeovers, hedging, pressure cleaning, privacy screening, Timber deck rejuvenation, Planting, Turf preparation and installation, and much more. Free no obligation quotes, reliable and friendly service, great rates. 12 years experience. Web www.tollmereyards.com.au - Phone 0418527036 - Email kip@tollmereyards.com.au I would like the design to portray a friendly and professional approach.

Target Market(s)

Residential

Industry/Entity Type

Gardener

Font styles to use
Serif

Colors
9ccb3b
abd037
3176b5

Requirements
Must have
• my services, my logo, my contact details,

```html
<!DOCTYPE html>
<html lang="en">
<head>
<meta charset="utf-8">
<title>Tollmere Yards – DL Flyer</title>
<link href="https://fonts.googleapis.com/css2?family=Roboto+Slab:wght@600;700&family=Lato:wght@400&family=Open+Sans:wght@600&family=Montserrat:wght@400;500&display=swap" rel="stylesheet">
<style>
  :root{
    --bg:#5f5f5f;
    --paper:#ffffff;
    --green:#2c7d32;
    --green-bright:#4aa82a;
    --lawn:#3f9a2e;
    --purple:#5c2362;
    --purple-head:#5e2466;
    --text:#222;
  }
  *{margin:0;padding:0;box-sizing:border-box}
  html,body{width:1200px;height:1200px;overflow:hidden;background:var(--bg)}
  .stage{position:relative;width:1200px;height:1200px}
  .flyer{position:absolute;top:184px;width:392px;height:832px;background:var(--paper);overflow:hidden}
  .flyer--front{left:126px}
  .flyer--back{left:620px}
  .abs{position:absolute}
  .photo{position:absolute;left:0;width:392px}
  .chevron{position:absolute;left:0;top:0}

  /* front */
  .brand-name{top:138px;left:0;width:100%;text-align:center;font:700 27px 'Roboto Slab',serif;color:var(--green)}
  .front-photo{top:187px;height:370px;background:linear-gradient(180deg,#eef0ee 0%,#8fb07a 14%,#4d7d36 30%,#c9728a 42%,#4ea32f 50%,#3d9a2c 100%)}
  .headline{top:404px;left:0;width:100%;text-align:center;font:700 23px/28px 'Roboto Slab',serif;color:#fff;letter-spacing:.2px}
  .welcome{top:538px;left:0;width:100%;text-align:center;font:700 23px/28px 'Roboto Slab',serif;color:var(--green)}
  .intro{top:616px;left:25px;width:342px;font:400 10.4px/14px 'Lato',sans-serif;color:var(--text);text-align:justify}
  .intro p{margin-bottom:13px}
  .rule{position:absolute;left:0;width:100%;height:3px;background:var(--green-bright)}
  .footer{position:absolute;left:0;bottom:0;width:100%;background:var(--purple);color:#fff;text-align:center;font:500 14px 'Montserrat',sans-serif;letter-spacing:1px}
  .front .rule{top:767px}

  /* back */
  .back-photo{top:0;height:420px;background:linear-gradient(180deg,#1fb2ef 0%,#6fcaf0 28%,#6c8c5a 42%,#d6cdb0 52%,#3f8a2a 66%,#4fb03a 100%)}
  .section-title{left:0;width:100%;text-align:center;font:700 20px 'Roboto Slab',serif;color:var(--purple-head)}
  .services{left:34px;width:340px;display:grid;grid-template-columns:174px 166px;font:600 11.6px/15px 'Open Sans',sans-serif;color:var(--text)}
  .services ul{list-style:none}
  .services li{position:relative;padding-left:20px;margin-bottom:10px}
  .services li::before{content:"";position:absolute;left:3px;top:1px;width:5px;height:10px;border:solid var(--green-bright);border-width:0 2px 2px 0;transform:rotate(40deg)}
  .contact{font:400 15px/22.5px 'Montserrat',sans-serif;letter-spacing:.4px;padding-top:15px}
  .contact .ic{display:inline-block;width:11px;height:11px;margin-right:6px;vertical-align:-1px}
</style>
</head>
<body>
<div class="stage">

  <section class="flyer flyer--front front">
    <div class="abs brand-name">Tollmere Yards</div>
    <div class="photo front-photo" role="img" aria-label="Photo of a landscaped garden with a wide green lawn, flower beds and tall trees"></div>
    <h1 class="abs headline">A BEAUTIFUL GARDEN<br>DOESN'T HAPPEN BY ITSELF</h1>
    <svg class="chevron" width="392" height="832" viewBox="0 0 392 832" aria-hidden="true">
      <polygon points="0,530 196,481 392,530 392,557 0,557" fill="var(--purple)"/>
      <polygon points="0,548 196,481 392,548 392,832 0,832" fill="var(--paper)"/>
    </svg>
    <h2 class="abs welcome">WELCOME TO<br>TOLLMERE YARDS</h2>
    <div class="abs intro">
      <p>Tollmere Yards is your garden &amp; lawn care specialist, with a passion for gardening and a keen eye for detail you can rest assured you're in the right hands.</p>
      <p>My services are tailored to meet every individual clients needs. From a one time mow too regular lawn mowing, all aspects of garden care and even full garden makeovers.</p>
      <p>I go that extra mile every time to leave you garden and yard looking amazing.</p>
    </div>
    <div class="rule"></div>
    <footer class="footer" style="height:61px;line-height:61px">www.tollmereyards.com.au</footer>
  </section>

  <section class="flyer flyer--back">
    <div class="photo back-photo" role="img" aria-label="Photo of a weatherboard house with a neat front lawn and rounded shrubs under a blue sky"></div>
    <svg class="chevron" width="392" height="832" viewBox="0 0 392 832" aria-hidden="true">
      <polygon points="0,405 196,346 392,405 392,425 0,425" fill="var(--purple)"/>
      <polygon points="0,424 196,346 392,424 392,832 0,832" fill="var(--paper)"/>
    </svg>

    <h2 class="abs section-title" style="top:422px">GARDEN SERVICES</h2>
    <div class="abs services" style="top:461px">
      <ul>
        <li>Lawn mowing</li>
        <li>Fertilizing</li>
        <li>Garden mulching</li>
        <li>Hedging</li>
        <li>Weeding</li>
      </ul>
      <ul>
        <li>Turf preparation and installation</li>
        <li>Tree and shrub pruning</li>
        <li>Full garden makeovers</li>
        <li>Green waste removal</li>
      </ul>
    </div>

    <h2 class="abs section-title" style="top:611px">OTHER SERVICES</h2>
    <div class="abs services" style="top:647px">
      <ul>
        <li>Aluminium fencing &amp; gate installation &amp; repairs</li>
        <li>Pressure cleaning</li>
      </ul>
      <ul>
        <li>Timber decking rejuvenation and repairs</li>
        <li>And much more!</li>
      </ul>
    </div>

    <div class="rule" style="top:731px"></div>
    <footer class="footer contact" style="height:98px">
      <div><svg class="ic" viewBox="0 0 12 12" aria-hidden="true"><path d="M2.5 1 L4.5 1 L5.2 3.6 L4 4.6 Q5 6.9 7.4 8 L8.4 6.8 L11 7.5 L11 9.5 Q10.5 11 9 11 Q1 10 1 2.5 Q1 1 2.5 1Z" fill="#9ccb3b"/></svg>0418527036</div>
      <div><svg class="ic" viewBox="0 0 12 12" aria-hidden="true"><rect x="1" y="3" width="10" height="7" fill="#9ccb3b"/><path d="M1 3 L6 7 L11 3" stroke="#5c2362" stroke-width="1" fill="none"/></svg>kip@tollmereyards.com.au</div>
      <div><svg class="ic" viewBox="0 0 12 12" aria-hidden="true"><circle cx="6" cy="6" r="4.8" fill="none" stroke="#9ccb3b" stroke-width="1.3"/><path d="M1.2 6 H10.8 M6 1.2 Q3 6 6 10.8 M6 1.2 Q9 6 6 10.8" stroke="#9ccb3b" stroke-width="1" fill="none"/></svg>www.tollmereyards.com.au</div>
    </footer>
  </section>

</div>
</body>
</html>
```